Maplewood Youth Relief Trust

I need a site for a not for profit organization. The site requires an about us page, current projects, get involved and a contact us page
our not for profit will focus on three projects at a time the three focus would be childrens cancer, sick children and disadvantaged children
our logo is red and white so something that will complement this color scheme

Coding

Coded - Design and coding required

Number of Pages Required

5+ page

Font styles to use
Sans Serif

Colors
ec1f27
33a6d7
fbed22

Requirements
Must have
• an about us, contact us, current projects, home page, and
• get involved pages
• ability to update our pages easily

```html
<!DOCTYPE html>
<html lang="en">
<head>
<meta charset="utf-8">
<title>Maplewood Youth Relief Trust</title>
<link href="https://fonts.googleapis.com/css2?family=Montserrat:wght@600&family=Open+Sans:wght@400;600;700&display=swap" rel="stylesheet">
<style>
  :root {
    --red: #ec1f27;
    --blue: #33a6d7;
    --blue-dark: #1f86b4;
    --yellow: #fbed22;
    --yellow-nav: #d9d21c;
    --text: #555;
    --text-light: #999;
    --ink: #3a3a3a;
    --rule: #dcdcdc;
    --footer-light: #f4f4f4;
    --footer-dark: #333;
    --white: #fff;
  }
  * { box-sizing: border-box; margin: 0; padding: 0; }
  html, body { width: 849px; height: 1200px; overflow: hidden; background: var(--white); }
  body { position: relative; font-family: "Open Sans", Arial, sans-serif; color: var(--text); }
  .abs { position: absolute; }

  .site-title { top: 14px; left: 0; width: 849px; text-align: center; font-family: "Montserrat", Arial, sans-serif; font-weight: 600; font-size: 22px; color: var(--red); letter-spacing: -0.2px; }

  .main-nav { top: 52px; left: 94px; width: 661px; height: 28px; background: var(--blue); display: flex; align-items: center; font-size: 9px; color: var(--white); }
  .main-nav .nav-item { padding: 0 15.5px; line-height: 28px; }
  .main-nav .nav-item.active { background: var(--yellow-nav); color: #555; width: 57px; text-align: center; padding: 0; }
  .nav-search { margin-left: auto; width: 119px; height: 28px; background: var(--blue-dark); display: flex; align-items: center; justify-content: space-between; padding: 0 9px 0 12px; font-size: 7.5px; color: #cfe8f4; }

  .hero { top: 80px; left: 94px; width: 661px; height: 272px; background: linear-gradient(90deg, #c9a27e 0%, #e8c4a4 30%, #f0d3b8 50%, #d8c6a8 70%, #b8c598 88%, #dfe5cf 100%); }
  .hero-tagline { top: 185px; right: 108px; text-align: right; font-family: "Open Sans", Arial, sans-serif; font-weight: 700; font-size: 19px; line-height: 24px; color: #1e1e1e; letter-spacing: 0.4px; }
  .hero-dots { top: 317px; left: 396px; width: 55px; height: 13px; border-radius: 7px; background: rgba(60,40,30,0.75); display: flex; align-items: center; justify-content: center; gap: 5px; }
  .hero-dots span { width: 5px; height: 5px; border-radius: 50%; background: var(--white); }
  .hero-dots span.current { background: transparent; border: 1px solid var(--white); }

  .intro { top: 368px; left: 94px; width: 661px; font-size: 12px; line-height: 18.4px; text-align: center; color: #666; }

  .focus-heading { top: 443px; left: 0; width: 849px; text-align: center; font-size: 11px; color: var(--blue); }
  .focus-area { top: 472px; width: 200px; display: flex; gap: 12px; }
  .focus-icon { flex: none; width: 46px; height: 46px; border-radius: 50%; background: var(--blue); display: flex; align-items: center; justify-content: center; }
  .focus-title { font-size: 12.5px; color: var(--blue); line-height: 14px; margin-bottom: 4px; }
  .focus-text { font-size: 6.2px; line-height: 10px; color: var(--text-light); }

  .motto-rule { top: 562px; left: 94px; width: 661px; height: 1px; background: var(--rule); }
  .motto { top: 545px; left: 235px; width: 377px; height: 35px; background: var(--white); border: 1px solid #d2d2d2; border-radius: 2px; font-size: 11.5px; color: #777; display: flex; align-items: center; justify-content: center; }

  .projects-heading { top: 597px; left: 0; width: 849px; text-align: center; font-size: 16px; color: var(--red); }
  .project { top: 634px; width: 203px; }
  .project-photo { height: 132px; }
  .project-caption { margin-top: 7px; font-size: 10.5px; color: #333; text-align: center; }

  .vision { top: 806px; left: 94px; width: 661px; height: 147px; background: linear-gradient(90deg, #8d8d8d 0%, #a5a5a5 35%, #6d5a55 55%, #9a8f8c 75%, #b2b2b2 100%); }
  .vision-title { top: 836px; left: 114px; font-size: 21px; font-weight: 700; color: var(--white); letter-spacing: 0.3px; }
  .vision-text { top: 864px; left: 116px; width: 170px; font-size: 10.3px; line-height: 14.8px; font-weight: 600; color: var(--white); }

  .volunteer { top: 980px; left: 0; width: 849px; text-align: center; font-size: 12.6px; font-weight: 700; color: #444; letter-spacing: 0.3px; }
  .cta { top: 1002px; left: 365px; width: 120px; height: 33px; background: var(--red); color: var(--yellow); font-weight: 700; font-size: 12.8px; display: flex; align-items: center; justify-content: center; }

  .contact-band { top: 1064px; left: 0; width: 849px; height: 62px; background: var(--footer-light); }
  .contact-item { top: 1090px; display: flex; align-items: center; gap: 6px; font-family: Arial, sans-serif; font-size: 8.2px; color: #666; }
  .social { top: 1086px; display: flex; gap: 7px; }
  .social span { width: 18px; height: 18px; border-radius: 50%; display: block; }
  .social .s1 { background: #3b5998; }
  .social .s2 { background: #33a6d7; }
  .social .s3 { background: #1f86b4; }

  .site-footer { top: 1126px; left: 0; width: 849px; height: 74px; background: var(--footer-dark); color: #ccc; font-size: 8px; text-align: center; }
  .footer-links { margin-top: 21px; }
  .footer-links span { padding: 0 6px; }
  .copyright { margin-top: 12px; }
</style>
</head>
<body>
  <div class="abs site-title">MAPLEWOOD YOUTH RELIEF TRUST</div>

  <nav class="abs main-nav">
    <span class="nav-item active">Home</span>
    <span class="nav-item">About us</span>
    <span class="nav-item">Current projects</span>
    <span class="nav-item">Project SickChildren</span>
    <span class="nav-item">Contact us</span>
    <span class="nav-item">Get Involved</span>
    <div class="nav-search">Search
      <svg width="9" height="9" viewBox="0 0 10 10"><circle cx="4" cy="4" r="3" fill="none" stroke="#fff" stroke-width="1.6"/><line x1="6.2" y1="6.2" x2="9" y2="9" stroke="#fff" stroke-width="1.8"/></svg>
    </div>
  </nav>

  <div class="abs hero" role="img" aria-label="Photo of laughing children close together outdoors"></div>
  <div class="abs hero-tagline">NO CHILD<br>SHOULD SUFFER</div>
  <div class="abs hero-dots"><span class="current"></span><span></span><span></span><span></span></div>

  <p class="abs intro">The Maplewood Youth Relief Trust is the federally registered charity for sick and disadvantaged children in Canada. Our aim is simple – we are working to empower children throughout Canada as they deal with the consequences of serious illness and complex situations.</p>

  <div class="abs focus-heading">We focus on three key areas</div>

  <div class="abs focus-area" style="left:94px">
    <div class="focus-icon">
      <svg width="20" height="22" viewBox="0 0 20 22" fill="none" stroke="#fff" stroke-width="1.8" stroke-linecap="round"><path d="M4 2v6a4 4 0 0 0 8 0V2"/><path d="M8 12v3a4 4 0 0 0 8 0v-3"/><circle cx="16" cy="10" r="2"/></svg>
    </div>
    <div><div class="focus-title">Health Care</div><div class="focus-text">Pellentesque habitant morbi tristique senectus et netus et malesuada fames ac turpis egestas. Nunc mollis, mi eu porta condimentum.</div></div>
  </div>
  <div class="abs focus-area" style="left:325px">
    <div class="focus-icon">
      <svg width="18" height="22" viewBox="0 0 18 22" fill="#fff"><rect x="2" y="2" width="1.5" height="7"/><rect x="5" y="2" width="1.5" height="7"/><rect x="8" y="2" width="1.5" height="7"/><rect x="2" y="8" width="7.5" height="3" rx="1"/><rect x="4.5" y="10" width="2.5" height="10" rx="1"/><path d="M12 2c3 0 4 4 4 8h-2v10h-2.5z"/></svg>
    </div>
    <div><div class="focus-title">Nutrition</div><div class="focus-text">Pellentesque habitant morbi tristique senectus et netus et malesuada fames ac turpis egestas. Nunc mollis, mi eu porta condimentum.</div></div>
  </div>
  <div class="abs focus-area" style="left:555px">
    <div class="focus-icon">
      <svg width="22" height="18" viewBox="0 0 22 18" fill="#fff"><circle cx="11" cy="4" r="3"/><circle cx="4.5" cy="6" r="2.3"/><circle cx="17.5" cy="6" r="2.3"/><path d="M6 16c0-4 2-7 5-7s5 3 5 7z"/><path d="M0.5 15c0-3 1.5-5.5 4-5.5 1 0 1.6.3 2 .7-1 1.3-1.5 3-1.5 4.8z"/><path d="M21.5 15c0-3-1.5-5.5-4-5.5-1 0-1.6.3-2 .7 1 1.3 1.5 3 1.5 4.8z"/></svg>
    </div>
    <div><div class="focus-title">Leadership Development</div><div class="focus-text">Pellentesque habitant morbi tristique senectus et netus et malesuada fames ac turpis egestas. Nunc mollis, mi eu porta condimentum.</div></div>
  </div>

  <div class="abs motto-rule"></div>
  <div class="abs motto">We have adopted the idea of "No child should suffer" for our work.</div>

  <h2 class="abs projects-heading" style="font-weight:400">Current projects</h2>

  <div class="abs project" style="left:94px">
    <div class="project-photo" role="img" aria-label="Photo of children running and jumping on grass" style="background:linear-gradient(180deg,#4f6b3a,#7a8f55 60%,#5c6e3c)"></div>
    <div class="project-caption">Project Disadvantaged Children awareness</div>
  </div>
  <div class="abs project" style="left:323px">
    <div class="project-photo" role="img" aria-label="Photo of young volunteers in red serving at a table" style="background:linear-gradient(180deg,#8a8a88,#5a4a48 55%,#b9b9b5)"></div>
    <div class="project-caption">Youth Clubs</div>
  </div>
  <div class="abs project" style="left:551px">
    <div class="project-photo" role="img" aria-label="Photo of a boy eating breakfast at a table" style="background:linear-gradient(180deg,#bcd9ea,#e3d2b4 55%,#efe6d8)"></div>
    <div class="project-caption">Breakfast Programs</div>
  </div>

  <div class="abs vision" role="img" aria-label="Photo of a woman and a boy in a wheelchair sharing a moment outdoors"></div>
  <h2 class="abs vision-title">OUR VISION</h2>
  <p class="abs vision-text">To foster Relationships with organizations whose programs support our children and youth to promote a more equitable and caring society.</p>

  <div class="abs volunteer">IF YOU’RE THINKING OF VOLUNTEERING AS AN INDIVIDUAL, WE HAVE MANY DIFFERENT WAYS TO HELP.</div>
  <div class="abs cta">GET INVOLVED</div>

  <div class="abs contact-band"></div>
  <div class="abs contact-item" style="left:94px">
    <svg width="7" height="10" viewBox="0 0 7 10"><path d="M3.5 0A3.5 3.5 0 0 0 0 3.5C0 6 3.5 10 3.5 10S7 6 7 3.5A3.5 3.5 0 0 0 3.5 0z" fill="#777"/><circle cx="3.5" cy="3.5" r="1.3" fill="#f4f4f4"/></svg>
    270 Birchline Ave, Kingsford, Ontario K0A 1B0
  </div>
  <div class="abs contact-item" style="left:306px">
    <svg width="9" height="9" viewBox="0 0 10 10"><path d="M2 0l2 2.5-1.2 1.3a6 6 0 0 0 3.4 3.4L7.5 6 10 8l-1.2 1.7C4.5 10 0 5.5.3 1.2z" fill="#777"/></svg>
    Call us on : 1 800 555-0147
  </div>
  <div class="abs contact-item" style="left:461px">
    <svg width="10" height="8" viewBox="0 0 10 8"><rect width="10" height="8" fill="#777"/><path d="M0 0l5 4 5-4" fill="none" stroke="#f4f4f4" stroke-width="1"/></svg>
    Email : hello@maplewoodyouthrelief.org
  </div>
  <div class="abs social" style="left:688px" aria-label="Social links"><span class="s1"></span><span class="s2"></span><span class="s3"></span></div>

  <footer class="abs site-footer">
    <div class="footer-links"><span>Home</span>|<span>About us</span>|<span>Current projects</span>|<span>Project Sick Children</span>|<span>Contact us</span>|<span>Get Involved</span></div>
    <div class="copyright">Copyright © 2016 Maplewood Youth Relief Trust. All rights reserved.</div>
  </footer>
</body>
</html>
```